business card design and letterhead for a building inspection company. We have a pre-purchase building and pest inspection ( i inspect house before people purchase it)
Updates

Linda has been so so responsive and good, i highly recommend her

Industry/Entity Type

Building

Contact Information for Business Card

audience, solicitor, real estate agent, mortgage brokerthe rest of the info will be in the attachement business card

```html
<!DOCTYPE html>
<html lang="en">
<head>
<meta charset="utf-8">
<title>Truframe Property Inspections – Business Card</title>
<link href="https://fonts.googleapis.com/css2?family=Open+Sans:wght@600;700&display=swap" rel="stylesheet">
<style>
  :root {
    --brand-blue: #1660c4;
    --ink: #111111;
    --card-black: #050505;
    --card-white: #ffffff;
    --faint-blue: #d3ddf0;
    --backdrop: #e9e6e1;
  }
  html, body {
    margin: 0;
    width: 1200px;
    height: 900px;
    overflow: hidden;
    background: var(--backdrop);
    font-family: "Open Sans", Arial, sans-serif;
  }
  .canvas { position: relative; width: 1200px; height: 900px; }

  .card {
    position: absolute;
    width: 600px;
    height: 343px;
    overflow: hidden;
    box-shadow: 0 10px 28px rgba(0,0,0,0.28);
  }

  /* Back of card */
  .card-back { left: 110px; top: 90px; background: var(--card-black); }
  .card-back .side-stripe {
    position: absolute; right: 0; top: 0;
    width: 128px; height: 100%;
    background: var(--brand-blue);
  }
  .card-back .brand { left: 70px; top: 128px; }

  /* Brand lockup: name in one colour, one weight, with a plain square */
  .brand {
    position: absolute;
    display: flex;
    align-items: center;
    gap: 14px;
    color: var(--brand-blue);
    font-weight: 700;
  }
  .brand-square {
    width: 46px; height: 46px;
    background: var(--brand-blue);
    flex: none;
  }
  .brand-name { line-height: 1; }
  .brand-name .word { display: block; font-size: 44px; letter-spacing: 3px; }
  .brand-name .sub { display: block; font-size: 15px; letter-spacing: 1.5px; margin-top: 5px; }

  /* Front of card */
  .card-front { left: 490px; top: 440px; background: var(--card-white); }
  .card-front .brand { left: 34px; top: 36px; }
  .card-front .brand-square { width: 34px; height: 34px; }
  .card-front .brand-name .word { font-size: 32px; letter-spacing: 2px; }
  .card-front .brand-name .sub { font-size: 11px; letter-spacing: 1.2px; margin-top: 4px; }

  .decor-circle {
    position: absolute;
    right: 40px; top: 52px;
    width: 150px; height: 150px;
    border-radius: 50%;
    border: 16px solid var(--faint-blue);
    box-sizing: border-box;
  }

  .holder {
    position: absolute;
    left: 34px; top: 168px;
    width: 360px;
    border-bottom: 2px solid var(--brand-blue);
    padding-bottom: 4px;
    color: var(--brand-blue);
    font-weight: 600;
    font-size: 19px;
    letter-spacing: 0.5px;
  }
  .contact-list {
    position: absolute;
    left: 34px; top: 208px;
    margin: 0; padding: 0;
    list-style: none;
    color: var(--ink);
    font-weight: 700;
    font-size: 16px;
    line-height: 25px;
  }
  .contact-list li { display: flex; align-items: center; gap: 9px; }
  .contact-icon { width: 15px; height: 15px; flex: none; }

  .base-band {
    position: absolute; left: 0; bottom: 0;
    width: 100%; height: 36px;
    background: var(--brand-blue);
  }
</style>
</head>
<body>
<div class="canvas">

  <section class="card card-back" aria-label="Business card, back">
    <div class="side-stripe"></div>
    <div class="brand">
      <span class="brand-square"></span>
      <span class="brand-name"><span class="word">TRUFRAME</span><span class="sub">PROPERTY INSPECTIONS</span></span>
    </div>
  </section>

  <section class="card card-front" aria-label="Business card, front">
    <div class="brand">
      <span class="brand-square"></span>
      <span class="brand-name"><span class="word">TRUFRAME</span><span class="sub">PROPERTY INSPECTIONS</span></span>
    </div>
    <div class="decor-circle"></div>

    <div class="holder">DANIEL HARTLEY</div>
    <ul class="contact-list">
      <li>
        <svg class="contact-icon" viewBox="0 0 16 16" aria-hidden="true"><rect width="16" height="16" fill="var(--brand-blue)"/><path d="M4.5 3.5l2 .2.6 2.3-1.2.9a6 6 0 0 0 3.2 3.2l.9-1.2 2.3.6.2 2c-4.5.6-8.6-3.5-8-8z" fill="#111"/></svg>
        (02) 5550 1842
      </li>
      <li>
        <svg class="contact-icon" viewBox="0 0 16 16" aria-hidden="true"><rect width="16" height="16" fill="var(--brand-blue)"/><rect x="5" y="3" width="6" height="10" rx="1" fill="none" stroke="#111" stroke-width="1.4"/></svg>
        0400 555 218
      </li>
      <li>
        <svg class="contact-icon" viewBox="0 0 16 16" aria-hidden="true"><rect width="16" height="16" fill="var(--brand-blue)"/><rect x="3" y="4.5" width="10" height="7" fill="#111"/><path d="M3 4.5l5 4 5-4" fill="none" stroke="#fff" stroke-width="1"/></svg>
        info@truframeinspections.com.au
      </li>
      <li>
        <svg class="contact-icon" viewBox="0 0 16 16" aria-hidden="true"><rect width="16" height="16" fill="var(--brand-blue)"/><circle cx="8" cy="8" r="4.5" fill="none" stroke="#111" stroke-width="1.3"/><path d="M3.5 8h9M8 3.5c-2 2.5-2 6.5 0 9M8 3.5c2 2.5 2 6.5 0 9" fill="none" stroke="#111" stroke-width="1"/></svg>
        www.truframeinspections.com.au
      </li>
    </ul>
    <div class="base-band"></div>
  </section>

</div>
</body>
</html>
```